Visitenkarten-Design für christliche Institution
Zielgruppe
Wir sind eine christliche Institution, die jungen Menschen im Alter von 17-30 Jahre helfen wollen, die Berufung in ihrem Leben zu finden.
Aufgabenstellung
Es sollte enhalten:
- Logo
- Adresse

```html
<!DOCTYPE html>
<html lang="de">
<head>
<meta charset="utf-8">
<title>Visitenkarte – Walk &amp; Find</title>
<link rel="stylesheet" href="https://fonts.googleapis.com/css2?family=Questrial&display=swap">
<style>
  :root {
    --stage: #b9bcbf;
    --paper: #fbfbfb;
    --ink: #2f2f33;
    --gold: #c9a13b;
    --night: #2d3b43;
    --night-deep: #1f2a30;
    --white: #f4f4f4;
  }
  * { box-sizing: border-box; margin: 0; padding: 0; }
  html, body { width: 1200px; height: 900px; overflow: hidden; }
  body {
    background: var(--stage);
    font-family: "Questrial", "Century Gothic", sans-serif;
    color: var(--ink);
    display: flex;
    flex-direction: column;
    align-items: center;
    justify-content: center;
    gap: 50px;
  }
  .card {
    width: 630px;
    height: 360px;
    position: relative;
    box-shadow: 0 10px 30px rgba(0,0,0,.18);
  }
  /* front */
  .card-front {
    background: var(--paper);
    border-bottom: 5px solid var(--gold);
  }
  .brand {
    position: absolute;
    left: 48px;
    top: 52px;
    display: flex;
    align-items: center;
    gap: 12px;
  }
  .brand-dot {
    width: 22px; height: 22px;
    border-radius: 50%;
    background: var(--gold);
  }
  .brand-name { font-size: 30px; color: var(--ink); letter-spacing: .5px; }
  .company {
    position: absolute;
    left: 48px; top: 170px; width: 240px;
    text-align: center;
  }
  .company-name { color: var(--gold); font-size: 19px; font-weight: 700; margin-bottom: 30px; }
  .company-address { font-size: 18px; line-height: 1.25; letter-spacing: .6px; }
  .divider {
    position: absolute;
    left: 318px; top: 150px;
    width: 2px; height: 130px;
    background: var(--gold);
  }
  .person {
    position: absolute;
    left: 350px; top: 120px;
  }
  .person-name { font-size: 21px; letter-spacing: .4px; }
  .person-role { font-size: 13px; color: #555; margin-top: 2px; }
  .contact { list-style: none; margin-top: 26px; }
  .contact li {
    display: flex; align-items: center; gap: 10px;
    font-size: 17px; letter-spacing: .6px; line-height: 1.35;
  }
  .contact svg { width: 14px; height: 14px; fill: var(--gold); flex: none; }
  /* back */
  .card-back {
    background: radial-gradient(circle at 50% 55%, #3c4c55 0%, var(--night) 45%, var(--night-deep) 100%);
    display: flex; align-items: center; justify-content: center;
  }
  .back-brand { display: flex; align-items: center; gap: 18px; }
  .back-brand .brand-dot { width: 34px; height: 34px; }
  .back-brand .brand-name { font-size: 48px; color: var(--white); }
</style>
</head>
<body>
  <section class="card card-front">
    <div class="brand">
      <span class="brand-dot"></span>
      <span class="brand-name">Walk &amp; Find</span>
    </div>
    <div class="company">
      <p class="company-name">Walk and Find Ltd</p>
      <p class="company-address">Lindenstraße 24<br>04109 Lindenau</p>
    </div>
    <div class="divider"></div>
    <div class="person">
      <p class="person-name">Jonas Keller</p>
      <p class="person-role">Geschäftsführer</p>
      <ul class="contact">
        <li><svg viewBox="0 0 16 16"><path d="M3 1l3 3-2 2c1 2 3 4 5 5l2-2 3 3-2 3C7 15 1 9 1 3z"/></svg>04711/208-519</li>
        <li><svg viewBox="0 0 16 16"><path d="M4 0h8a1 1 0 011 1v14a1 1 0 01-1 1H4a1 1 0 01-1-1V1a1 1 0 011-1zm1 2v10h6V2zm3 11a1 1 0 100 2 1 1 0 000-2z"/></svg>015209347718</li>
        <li><svg viewBox="0 0 16 16"><path d="M0 3h16v10H0zm1 1v.5l7 5 7-5V4z"/></svg>jonas.keller@weg-lindenau.de</li>
      </ul>
    </div>
  </section>

  <section class="card card-back">
    <div class="back-brand">
      <span class="brand-dot"></span>
      <span class="brand-name">Walk &amp; Find</span>
    </div>
  </section>
</body>
</html>
```